Stationery & Business Card Design For A Mobile Ultrasound Company
Ridgecrest Sonar Partners, Inc.
Professional
Martin L. Povich
Clinical Director
3187 Hawthorn Lane NE
Carrollton, OH 44892
ridgecrestsonarpartners@mailnest.example
www.ridgecrestsonarpartners.example

```html
<!DOCTYPE html>
<html lang="en">
<head>
<meta charset="utf-8">
<title>Ridgecrest Sonar Partners — Business Card</title>
<link rel="stylesheet" href="https://fonts.googleapis.com/css2?family=Arimo:wght@400;700&display=swap">
<style>
  :root {
    --backdrop: #2a2a2a;
    --card: #f7f7f7;
    --brand-blue: #1d5fae;
    --brand-red: #d02a35;
    --ink: #2b2b2b;
    --ink-soft: #555555;
    --rule: #c9c9c9;
  }
  * { margin: 0; padding: 0; box-sizing: border-box; }
  html, body {
    width: 1200px;
    height: 901px;
    overflow: hidden;
    background: var(--backdrop);
    font-family: "Arimo", Arial, sans-serif;
  }
  .stage {
    width: 1200px;
    height: 901px;
    display: flex;
    align-items: center;
    justify-content: center;
  }
  .business-card {
    position: relative;
    width: 980px;
    height: 560px;
    background: var(--card);
    box-shadow: 0 12px 40px rgba(0,0,0,0.45);
  }
  .edge-band {
    position: absolute;
    top: 0;
    bottom: 0;
    width: 42px;
  }
  .edge-band--left { left: 0; background: var(--brand-blue); }
  .edge-band--right { right: 0; background: var(--brand-red); }

  .brand {
    position: absolute;
    left: 100px;
    top: 150px;
    display: flex;
    align-items: center;
    gap: 16px;
  }
  .brand-dot {
    width: 34px;
    height: 34px;
    border-radius: 50%;
    background: var(--brand-red);
    flex: none;
  }
  .brand-name {
    font-size: 46px;
    font-weight: 400;
    color: var(--brand-blue);
    letter-spacing: 0.5px;
    white-space: nowrap;
  }

  .person {
    position: absolute;
    left: 100px;
    top: 350px;
  }
  .person-name {
    font-size: 20px;
    font-weight: 700;
    color: var(--ink);
  }
  .person-title {
    margin-top: 6px;
    font-size: 17px;
    color: var(--ink-soft);
  }

  .contact {
    position: absolute;
    left: 470px;
    top: 270px;
    padding-left: 22px;
    border-left: 1px solid var(--rule);
    font-size: 17px;
    line-height: 25px;
    color: var(--ink-soft);
  }
  .contact-address { margin-bottom: 8px; }
  .contact-label {
    display: inline-block;
    width: 22px;
  }
</style>
</head>
<body>
<main class="stage">
  <article class="business-card">
    <div class="edge-band edge-band--left"></div>
    <div class="edge-band edge-band--right"></div>

    <header class="brand">
      <span class="brand-name">Ridgecrest Sonar Partners</span>
      <span class="brand-dot"></span>
    </header>

    <section class="person">
      <p class="person-name">Martin L. Povich</p>
      <p class="person-title">Clinical Director</p>
    </section>

    <section class="contact">
      <p class="contact-address">3187 Hawthorn Lane NE<br>Carrollton, OH 44892</p>
      <p><span class="contact-label">P :</span>330-555-0186</p>
      <p><span class="contact-label">C :</span>330-555-0142</p>
      <p><span class="contact-label">E :</span>ridgecrestsonarpartners@mailnest.example</p>
      <p><span class="contact-label">w :</span>www.ridgecrestsonarpartners.example</p>
    </section>
  </article>
</main>
</body>
</html>
```